Legal Agribusiness Capability Brochure Design

Design A4 sized 6 page Legal Agribusiness Capability Brochure. Design is to be consistent with current marketing materials - logo, letterhead, website and business card to be provided.
Cover page - Firm name and logo, Agribusiness Capability Statement heading with image 1 below
Inside cover page - About Us section with image 2 below then Awards section below image
Inside middle page - Our Expertise with image 3 below
Inside back page - Our Experience with image 4 below
Back page - Senior Lawyers with image 5 below
Outside Middle Back Page - Contact Us with image 6
Updates

To provide more details to designers for brochure

Target Market(s)

Agribusiness - Australia

Industry/Entity Type

Legal

Colors

Designer to choose colors to be used in the design.

Requirements
Must have
• Use content from uloaded file - Agribusiness Brochure Content
• Use images uploaded
• Professional appearance
• Consistent with current marketing and website https://ferngatelegal.com.au/

```html
<!DOCTYPE html>
<html lang="en">
<head>
<meta charset="utf-8">
<title>Ferngate Legal – Agribusiness Capability Brochure</title>
<link href="https://fonts.googleapis.com/css2?family=Roboto:wght@400;500;700&display=swap" rel="stylesheet">
<style>
  :root {
    --stage-blue: #0b80c3;
    --brand-blue: #1a7cc4;
    --heading-grey: #5f6062;
    --text-grey: #555759;
    --paper: #ffffff;
  }
  * { margin: 0; padding: 0; box-sizing: border-box; }
  html, body { width: 1200px; height: 1133px; overflow: hidden; }
  body {
    background: var(--stage-blue);
    font-family: "Roboto", Arial, sans-serif;
    position: relative;
  }
  .page {
    position: absolute;
    width: 319px;
    height: 451px;
    background: var(--paper);
    overflow: hidden;
    box-shadow: 0 3px 10px rgba(0, 0, 0, 0.28);
  }
  .page--cover      { left: 80px;  top: 86px; }
  .page--about      { left: 442px; top: 86px; }
  .page--expertise  { left: 804px; top: 86px; }
  .page--experience { left: 80px;  top: 595px; }
  .page--people     { left: 442px; top: 595px; }
  .page--back       { left: 804px; top: 595px; }

  .section-title {
    position: absolute;
    left: 26px;
    font-size: 10px;
    font-weight: 700;
    color: var(--brand-blue);
    letter-spacing: 0.1px;
  }
  .section-tab {
    position: absolute;
    left: 0;
    width: 23px;
    height: 9px;
    background: var(--brand-blue);
    border-radius: 0 4px 4px 0;
  }

  .body-text {
    position: absolute;
    left: 23px;
    font-size: 5.2px;
    line-height: 6.4px;
    color: var(--text-grey);
  }
  .bullet-list {
    position: absolute;
    left: 23px;
    list-style: none;
    font-size: 5.2px;
    line-height: 9.7px;
    color: var(--brand-blue);
  }
  .bullet-list li { position: relative; padding-left: 6px; }
  .bullet-list li::before {
    content: "";
    position: absolute;
    left: 0; top: 3.6px;
    width: 2.6px; height: 2.6px;
    background: var(--brand-blue);
  }

  .photo { position: absolute; left: 0; width: 319px; }
  .photo--harvester { top: 208px; height: 204px; background: linear-gradient(180deg, #b7a491 0%, #cfa75a 45%, #b98a3e 100%); }
  .photo--pumpkins  { top: 150px; height: 150px; background: radial-gradient(ellipse at 45% 70%, #e07a22 0%, #b85a17 55%, #4a3528 100%); }
  .photo--lamb      { top: 349px; height: 102px; background: linear-gradient(180deg, #5d7a3a 0%, #7f9e4a 55%, #4d6a2c 100%); }
  .photo--aerial    { top: 226px; height: 225px; background: linear-gradient(135deg, #c9a94a 0%, #7a7a82 45%, #c3a545 70%, #6a6c80 100%); }
  .photo--machinery { top: 151px; height: 150px; background: linear-gradient(180deg, #c7cbd0 0%, #dadbd8 40%, #b9a76e 70%, #c8a862 100%); }
  .photo--grain     { top: 208px; height: 243px; background: radial-gradient(ellipse at 55% 45%, #c9a36b 0%, #8d6a43 50%, #4f3924 100%); }

  .wheat-band {
    position: absolute;
    left: 0; top: 412px;
    width: 319px; height: 39px;
    background: linear-gradient(180deg, #1b8cc9 0%, #0f6fa6 100%);
  }

  .badge {
    position: absolute;
    width: 57px; height: 57px;
    border-radius: 50%;
    background: #ffffff;
    border: 2px solid var(--brand-blue);
    box-shadow: 0 0 0 2px #ffffff;
  }

  .brand {
    position: absolute;
    display: flex;
    align-items: center;
    gap: 5px;
  }
  .brand__mark { width: 30px; height: 30px; background: var(--brand-blue); }
  .brand__name {
    font-size: 15px;
    font-weight: 500;
    color: var(--brand-blue);
    line-height: 1;
  }
  .brand__sub {
    font-size: 7px;
    font-weight: 500;
    color: var(--brand-blue);
    margin-top: 3px;
  }

  .cover-heading {
    position: absolute;
    font-size: 11.5px;
    font-weight: 500;
    color: var(--heading-grey);
  }

  .person-name { color: var(--brand-blue); font-weight: 700; }
  .person-role { color: var(--brand-blue); font-size: 3.4px; }

  .contact-col {
    position: absolute;
    top: 351px;
    font-size: 5px;
    line-height: 6.3px;
    color: var(--text-grey);
  }
  .contact-col h4 {
    font-size: 5.2px;
    font-weight: 700;
    color: var(--brand-blue);
    margin-bottom: 6px;
  }
  .contact-row {
    display: flex;
    gap: 5px;
    align-items: flex-start;
    margin-bottom: 6.5px;
  }
  .contact-row svg { width: 7px; height: 7px; flex: none; }
</style>
</head>
<body>

<section class="page page--cover">
  <div class="brand" style="left: 89px; top: 132px;">
    <span class="brand__mark"></span>
    <div>
      <div class="brand__name">FERNGATE LEGAL</div>
      <div class="brand__sub">Commercial + Litigation</div>
    </div>
  </div>
  <h1 class="cover-heading" style="left: 76px; top: 193px;">Agribusiness Capability Statement</h1>
  <div class="photo photo--harvester" role="img" aria-label="Yellow combine harvester in a wheat field under a cloudy sky"></div>
  <div class="wheat-band" role="img" aria-label="Wheat stalks tinted blue"></div>
  <div class="badge" style="left: 131px; top: 373px;"></div>
</section>

<section class="page page--about">
  <span class="section-tab" style="top: 24px;"></span>
  <h2 class="section-title" style="top: 23px;">About</h2>
  <p class="body-text" style="top: 44px; width: 270px;">Ferngate Legal is a leading independent law firm with offices in Kalgara and Perth, Western Australia, specialising in:</p>
  <ul class="bullet-list" style="top: 62px;">
    <li>Business and Commercial</li>
    <li>Agribusiness and Rural</li>
    <li>Property and Leasing</li>
    <li>Fishing</li>
    <li>Wills and Estates</li>
    <li>Estate Disputes</li>
    <li>Litigation</li>
  </ul>
  <div class="photo photo--pumpkins" role="img" aria-label="Close-up of orange pumpkins"></div>
  <span class="section-tab" style="top: 326px;"></span>
  <h2 class="section-title" style="top: 324px;">Awards</h2>
  <p class="body-text" style="top: 345px;">We are proud be having the following awards:</p>
  <ul class="bullet-list" style="top: 356px;">
    <li>ranked as a “Leading Agribusiness Law Firm” - Western Australia 2017 (Top 5 in W.A.) by Harlow Guide</li>
    <li>awarded the Quality Practice Standard by the State Law Council of Western Australia</li>
    <li>ranked as a “Leading Agribusiness law Firm” - Western Australia 2018 (Top 4 in W.A.)</li>
    <li>ranked as a “Leading Agribusiness law Firm” - Western Australia 2019 (Top 4 in W.A.)</li>
  </ul>
</section>

<section class="page page--expertise">
  <span class="section-tab" style="top: 24px;"></span>
  <h2 class="section-title" style="top: 23px;">Agri business expertise</h2>
  <p class="body-text" style="top: 44px; width: 272px;">Over the years our senior lawyers have acted for clients involved in wheat, canola, lupin, wool, beef, dairy, lamb, poultry, piggery, viticulture, forestry and plantation operations. Our senior lawyers have strong family connections with various agribusiness operators which allows them to better appreciate the challenges faced in agribusiness.</p>
  <p class="body-text" style="top: 70px;">We can assist with the following agribusiness and rural matters:</p>
  <ul class="bullet-list" style="top: 82px; width: 276px;">
    <li>Agribusiness and rural property contracts, agreements and deeds</li>
    <li>Sale and purchase of farmland, agribusiness assets and livestock, including due diligence, pre-contractual negotiations, contract preparation, contract review and settlement</li>
    <li>Rural and agribusiness succession planning, including intergenerational farm transfers and Family Farm Exemption Transfers under the Duties Act 2008 (WA)</li>
    <li>Restructuring to facilitate succession planning</li>
    <li>Farm Leases, Share Farming Agreements and Livestock Management Agreements</li>
    <li>Pastoral leases and dealings with the Pastoral Lands Board</li>
    <li>Foreign Investment Review Board (FIRB) advice and applications</li>
    <li>Farm subdivisions</li>
    <li>Land dealings with mining, energy and telecommunications companies, including lease and licence agreements, wind farm agreements, royalty agreements, land access agreements, compensation agreements and easement deeds</li>
    <li>Compulsory acquisitions and land valuation matters</li>
    <li>Structuring advice on issues relating to trading entities, partnerships, trusts, corporations, joint ventures, syndicates and family restructures</li>
    <li>Trust deeds for holding and trading entities</li>
    <li>Preparation of partnership agreements</li>
    <li>Property ownership agreements</li>
    <li>Preparation of trust deeds for holding and trading entities</li>
    <li>Mortgages, crop liens and other securities against rural and agribusiness assets</li>
    <li>Water rights, access and licences under the Waterways Conservation Act 1976 (WA)</li>
    <li>Carbon trading agreements</li>
    <li>Employment Agreement</li>
    <li>Contractor Agreements</li>
    <li>Litigation</li>
  </ul>
  <div class="photo photo--lamb" role="img" aria-label="Young lamb standing in green grass"></div>
</section>

<section class="page page--experience">
  <span class="section-tab" style="top: 24px;"></span>
  <h2 class="section-title" style="top: 23px;">Agri business experience</h2>
  <p class="body-text" style="top: 46px; width: 275px;">Our senior lawyers have over 60 years combined experience in advising a diverse range of clients such as governments and government bodies, listed public companies, private companies, accounting practices, insurance and financial service firms, agribusiness operators, horticulture operators, fishing operators, property developers and investors, real estate agents and settlement agents, mining companies and investors, hospital operators, SME’s, sole traders and high net individual clients on commercial and litigation issues relating to the following industries:</p>
  <ul class="bullet-list" style="top: 84px;">
    <li>Agriculture</li>
    <li>Fisheries</li>
    <li>Forestry</li>
    <li>Mining</li>
    <li>Manufacturing</li>
    <li>Transport</li>
    <li>Hospitality</li>
    <li>Tourism</li>
    <li>Property</li>
    <li>Construction</li>
    <li>Franchising</li>
    <li>Service industries</li>
  </ul>
  <div class="photo photo--aerial" role="img" aria-label="Aerial view of a harvester working striped crop rows"></div>
  <div class="badge" style="left: 207px; top: 196px;"></div>
</section>

<section class="page page--people">
  <span class="section-tab" style="top: 24px;"></span>
  <h2 class="section-title" style="top: 23px;">Our people</h2>
  <p class="body-text" style="top: 45px; width: 270px;">
    <span class="person-name">Daniel Corrow</span> <span class="person-role">(Principal)</span><br>
    Daniel is the Principal of Ferngate Legal and has over 20 years’ experience in advising clients in a wide range of commercial law matters.<br>
    In 1998, Daniel was awarded a Certificate of Achievement in the Commercial &amp; Corporate Law Stream at Coastal University.<br>
    In 2019, Daniel was ranked as a “Preeminent Agribusiness Lawyer – Western Australia, 2019” (Top 2 in W.A.) by Harlow’s Guide
  </p>
  <p class="body-text" style="top: 102px; width: 270px;">
    <span class="person-name">Peter Corrow</span> <span class="person-role">(Consultant)</span><br>
    Peter is the Consultant at Ferngate Legal and has over 40 years’ experience in advising clients in commercial law matters, with considerable experience in litigation and disputes.
  </p>
  <div class="photo photo--machinery" role="img" aria-label="Combine harvester unloading grain into a tractor trailer"></div>
  <span class="section-tab" style="top: 326px;"></span>
  <h2 class="section-title" style="top: 324px;">Contact</h2>

  <div class="contact-col" style="left: 23px;">
    <h4>Kalgara Office</h4>
    <div class="contact-row">
      <svg viewBox="0 0 10 10"><path d="M5 0.5 A3.3 3.3 0 0 1 8.3 3.8 C8.3 6 5 9.5 5 9.5 C5 9.5 1.7 6 1.7 3.8 A3.3 3.3 0 0 1 5 0.5 Z M5 2.5 A1.3 1.3 0 1 0 5 5.1 A1.3 1.3 0 1 0 5 2.5 Z" fill="var(--brand-blue)" fill-rule="evenodd"/></svg>
      <span>Suite 4, Harbour House<br>12 Quayside Lane<br>Kalgara WA 6530</span>
    </div>
    <div class="contact-row">
      <svg viewBox="0 0 10 10"><rect x="2.5" y="0.5" width="5" height="9" rx="0.8" fill="none" stroke="var(--brand-blue)" stroke-width="1.2"/></svg>
      <span>+61 8 9000 1240</span>
    </div>
    <div class="contact-row">
      <svg viewBox="0 0 10 10"><rect x="1" y="1" width="3" height="8" fill="var(--brand-blue)"/><rect x="5" y="3" width="4" height="6" fill="var(--brand-blue)"/></svg>
      <span>+ 61 8 9000 1241</span>
    </div>
    <div class="contact-row">
      <svg viewBox="0 0 10 10"><rect x="0.6" y="2" width="8.8" height="6" fill="none" stroke="var(--brand-blue)" stroke-width="1"/><path d="M0.6 2 L5 5.5 L9.4 2" fill="none" stroke="var(--brand-blue)" stroke-width="1"/></svg>
      <span>info@ferngatelegal.com.au</span>
    </div>
  </div>

  <div class="contact-col" style="left: 126px;">
    <h4>Perth Office</h4>
    <div class="contact-row">
      <svg viewBox="0 0 10 10"><path d="M5 0.5 A3.3 3.3 0 0 1 8.3 3.8 C8.3 6 5 9.5 5 9.5 C5 9.5 1.7 6 1.7 3.8 A3.3 3.3 0 0 1 5 0.5 Z M5 2.5 A1.3 1.3 0 1 0 5 5.1 A1.3 1.3 0 1 0 5 2.5 Z" fill="var(--brand-blue)" fill-rule="evenodd"/></svg>
      <span>18 Calder Avenue<br>West Perth WA 6005</span>
    </div>
    <div class="contact-row">
      <svg viewBox="0 0 10 10"><rect x="2.5" y="0.5" width="5" height="9" rx="0.8" fill="none" stroke="var(--brand-blue)" stroke-width="1.2"/></svg>
      <span>+61 8 9000 2250</span>
    </div>
    <div class="contact-row">
      <svg viewBox="0 0 10 10"><rect x="1" y="1" width="3" height="8" fill="var(--brand-blue)"/><rect x="5" y="3" width="4" height="6" fill="var(--brand-blue)"/></svg>
      <span>+ 61 8 9000 2251</span>
    </div>
    <div class="contact-row">
      <svg viewBox="0 0 10 10"><rect x="0.6" y="2" width="8.8" height="6" fill="none" stroke="var(--brand-blue)" stroke-width="1"/><path d="M0.6 2 L5 5.5 L9.4 2" fill="none" stroke="var(--brand-blue)" stroke-width="1"/></svg>
      <span>info@ferngatelegal.com.au</span>
    </div>
  </div>

  <div class="contact-col" style="left: 227px; width: 70px;">
    <h4>All correspondence to be sent to</h4>
    <div class="contact-row">
      <svg viewBox="0 0 10 10"><path d="M5 0.5 A3.3 3.3 0 0 1 8.3 3.8 C8.3 6 5 9.5 5 9.5 C5 9.5 1.7 6 1.7 3.8 A3.3 3.3 0 0 1 5 0.5 Z M5 2.5 A1.3 1.3 0 1 0 5 5.1 A1.3 1.3 0 1 0 5 2.5 Z" fill="var(--brand-blue)" fill-rule="evenodd"/></svg>
      <span>PO Box 4120<br>Kalgara WA 6531</span>
    </div>
  </div>
</section>

<section class="page page--back">
  <div class="brand" style="left: 89px; top: 131px;">
    <span class="brand__mark"></span>
    <div>
      <div class="brand__name">FERNGATE LEGAL</div>
      <div class="brand__sub">Commercial + Litigation</div>
    </div>
  </div>
  <h2 class="cover-heading" style="left: 77px; top: 193px;">Leading Agribusiness Law Firm</h2>
  <div class="photo photo--grain" role="img" aria-label="Close-up of golden barley ears"></div>
</section>

</body>
</html>
```